Graphics for Book geared to Professionals

We need the attached graphics professional recreated for our book. The book will be in black and white so it will need to be grey scale. Please see the best practices for graphics from our publisher Harlow.
The power point attached has several graphics that we need professional illustrated. The graphics in a excel format simply need to be transposed professionally (slides 8-14). The graphs in the other slides need to have some design put behind them. These make the general look and feel somewhat consistent. If you have any questions, you can email me at marcus.thorne@velquist.com.

Target Market(s)

Professionals, Business Analyst

Industry/Entity Type

It Professional

Font styles to use
Other font styles liked:
• Calibre

Requirements
Must have
• Professional looks and feel

```html
<!DOCTYPE html>
<html lang="en">
<head>
<meta charset="utf-8">
<title>Analytical Cycle</title>
<link rel="stylesheet" href="https://fonts.googleapis.com/css2?family=Carlito:wght@400;700&display=swap">
<style>
  :root {
    --ink: #111111;
    --paper: #ffffff;
    --frame: #8a8a8a;
    --sphere-light: #f4f4f4;
    --sphere-mid: #d6d6d6;
    --sphere-dark: #a9a9a9;
    --arrow-dark: #3a3a3a;
    --arrow-light: #e2e2e2;
  }
  html, body {
    margin: 0;
    padding: 0;
    overflow: hidden;
    background: var(--paper);
  }
  .canvas {
    position: relative;
    width: 1074px;
    height: 1200px;
    overflow: hidden;
    background: var(--paper);
    font-family: "Carlito", "Calibri", sans-serif;
    color: var(--ink);
  }
  .frame {
    position: absolute;
    inset: 6px;
    border: 3px solid var(--frame);
  }
  .cycle-title {
    position: absolute;
    top: 52px;
    left: 0;
    width: 100%;
    margin: 0;
    text-align: center;
    font-size: 72px;
    font-weight: 700;
    letter-spacing: 1px;
  }
  .cycle-art {
    position: absolute;
    top: 0;
    left: 0;
  }
  .stage-label {
    position: absolute;
    width: 280px;
    margin-left: -140px;
    text-align: center;
    font-size: 28px;
    line-height: 1.18;
    transform: translateY(-50%);
  }
  .stage-label strong { font-weight: 700; }
  .stage-results { left: 257px; top: 300px; }
  .stage-information { left: 829px; top: 300px; }
  .stage-diagnose { left: 829px; top: 890px; }
  .stage-actions { left: 257px; top: 886px; }
</style>
</head>
<body>
<div class="canvas">
  <div class="frame"></div>
  <h1 class="cycle-title">ANALYTICAL CYCLE</h1>

  <svg class="cycle-art" width="1074" height="1200" viewBox="0 0 1074 1200" aria-hidden="true">
    <defs>
      <radialGradient id="sphere-fill" cx="0.4" cy="0.35" r="0.7">
        <stop offset="0" stop-color="var(--sphere-light)"/>
        <stop offset="0.65" stop-color="var(--sphere-mid)"/>
        <stop offset="1" stop-color="var(--sphere-dark)"/>
      </radialGradient>
      <linearGradient id="arrow-fill" x1="0" y1="0" x2="1" y2="0">
        <stop offset="0" stop-color="var(--arrow-light)"/>
        <stop offset="0.55" stop-color="var(--arrow-dark)"/>
        <stop offset="1" stop-color="#5c5c5c"/>
      </linearGradient>
      <filter id="soft-shadow" x="-20%" y="-20%" width="150%" height="150%">
        <feDropShadow dx="6" dy="8" stdDeviation="7" flood-color="#000" flood-opacity="0.35"/>
      </filter>
      <path id="cycle-arrow" d="M0,-22 Q100,-34 200,-22 L200,-52 L262,0 L200,52 L200,22 Q100,10 0,22 Z"/>
    </defs>

    <g class="arrows" fill="url(#arrow-fill)" filter="url(#soft-shadow)">
      <use href="#cycle-arrow" transform="translate(400,215) rotate(8)"/>
      <use href="#cycle-arrow" transform="translate(900,475) rotate(98)"/>
      <use href="#cycle-arrow" transform="translate(690,965) rotate(186)"/>
      <use href="#cycle-arrow" transform="translate(180,725) rotate(-88)"/>
    </g>

    <g class="spheres" fill="url(#sphere-fill)" filter="url(#soft-shadow)">
      <circle cx="257" cy="300" r="177"/>
      <circle cx="829" cy="300" r="177"/>
      <circle cx="829" cy="890" r="177"/>
      <circle cx="257" cy="886" r="177"/>
    </g>
  </svg>

  <p class="stage-label stage-results">Higher quality Actions yields improved Results and <strong>Measure</strong>ments</p>
  <p class="stage-label stage-information">Accurate<br>&amp;<br>Relevant<br><strong>Information</strong></p>
  <p class="stage-label stage-diagnose"><strong>Diagnose</strong><br>an opportunity to make better Decisions</p>
  <p class="stage-label stage-actions">Better Decisions yield higher quality <strong>Actions</strong></p>
</div>
</body>
</html>
```